Tarvell homes and renovations business card design.

Would like some new card designs utilizing my new logo that look professional. I am open to different colors on the logo or utilize the same ones we have. I like the original concept but would like to see some fresh ideas and build on what we have already done.

Target Market(s)

Custom home building industry, Real estate sales, Renovation projects.

Industry/Entity Type

Home Builder

Contact Information for Business Card

Tarvell Homes and Renovations
2871 162nd Street
Frank, Alberta
T0L3P0
Home : 403- 555-0187 Cell: 403- 555-0243

My info is : Gus Tarvell, President and CEO
email: tarvellhomes@quillmail.example
Website: tarvellhomes.example

Requirements
Must have
• Must Use my new logo design. I am open to different colors on the logo or utilize the same ones in the existing design. I can upload the original logo design if needed.

```html
<!DOCTYPE html>
<html lang="en">
<head>
<meta charset="utf-8">
<title>Tarvell Homes and Renovations – Business Card</title>
<link href="https://fonts.googleapis.com/css2?family=Montserrat:wght@700&family=Oswald:wght@500&family=Open+Sans:wght@400;600&display=swap" rel="stylesheet">
<style>
  :root {
    --backdrop: #2a2a2a;
    --gold-light: #f6c030;
    --gold-deep: #c08d35;
    --gold-text: #b8862b;
    --ink: #3b3b3b;
    --ink-soft: #5c5c5c;
    --paper: #ffffff;
    --rule: #8a8a8a;
  }
  * { box-sizing: border-box; margin: 0; padding: 0; }
  html, body {
    width: 1200px; height: 1000px; overflow: hidden;
    background: var(--backdrop);
  }
  .sheet {
    width: 1200px; height: 1000px;
    display: flex; flex-direction: column; align-items: center; justify-content: center;
    gap: 40px;
  }
  .card {
    width: 735px; height: 420px;
    box-shadow: 0 10px 30px rgba(0,0,0,.45);
    position: relative;
  }
  /* Front */
  .card-front {
    background: linear-gradient(180deg, var(--gold-light) 0%, var(--gold-deep) 100%);
    display: flex; align-items: center; justify-content: center;
  }
  .brand-name {
    font-family: "Montserrat", sans-serif;
    font-weight: 700;
    font-size: 30px;
    letter-spacing: 1px;
    text-transform: uppercase;
    color: var(--ink);
    text-align: center;
    line-height: 1.25;
  }
  /* Back */
  .card-back { background: var(--paper); }
  .identity {
    position: absolute; left: 0; top: 150px;
    width: 320px; text-align: right;
  }
  .person-name {
    font-family: "Oswald", sans-serif;
    font-weight: 500;
    font-size: 44px;
    letter-spacing: 1px;
    color: var(--ink-soft);
    line-height: 1;
  }
  .person-role {
    font-family: "Open Sans", sans-serif;
    font-weight: 600;
    font-size: 18px;
    color: var(--gold-text);
    margin-top: 4px;
  }
  .divider {
    position: absolute; left: 345px; top: 150px;
    width: 2px; height: 78px; background: var(--rule);
  }
  .contact-list {
    position: absolute; left: 368px; top: 146px;
    list-style: none;
    font-family: "Open Sans", sans-serif;
    font-size: 19px; color: var(--ink-soft);
  }
  .contact-list li {
    display: flex; align-items: center; gap: 12px;
    height: 23px;
  }
  .contact-list svg { width: 14px; height: 14px; fill: var(--gold-text); flex: none; }
  .web-accent { color: var(--gold-text); }
  .address {
    position: absolute; left: 0; right: 0; bottom: 70px;
    display: flex; justify-content: center; align-items: center; gap: 10px;
    font-family: "Open Sans", sans-serif;
    font-size: 19px; color: var(--ink-soft);
  }
  .address svg { width: 20px; height: 20px; fill: none; stroke: var(--gold-text); stroke-width: 1.6; }
</style>
</head>
<body>
<main class="sheet">
  <section class="card card-front">
    <p class="brand-name">Tarvell<br>Homes and Renovations</p>
  </section>

  <section class="card card-back">
    <div class="identity">
      <h1 class="person-name">GUS TARVELL</h1>
      <p class="person-role">President and CEO</p>
    </div>
    <div class="divider"></div>
    <ul class="contact-list">
      <li>
        <svg viewBox="0 0 16 16" aria-hidden="true"><path d="M3.6 1.2l2.3 2.6-1.3 1.9c.9 2 2.6 3.8 4.7 4.8l1.9-1.3 2.6 2.3-1.2 2.3C7.4 14.6 1.4 8.6 1.2 2.4z"/></svg>
        <span>403 555 0187</span>
      </li>
      <li>
        <svg viewBox="0 0 16 16" aria-hidden="true"><path d="M4.5 1h7v14h-7zM5.7 2.3v10h4.6v-10z"/></svg>
        <span>403 555 0243</span>
      </li>
      <li>
        <svg viewBox="0 0 16 16" aria-hidden="true"><path d="M1 3.5h14v9H1zM1.6 4l6.4 5 6.4-5z"/></svg>
        <span>tarvellhomes@quillmail.example</span>
      </li>
      <li>
        <svg viewBox="0 0 16 16" aria-hidden="true"><path d="M9.5 1.5a5 5 0 1 1 0 10 5 5 0 0 1 0-10zm0 1.6a3.4 3.4 0 1 0 0 6.8 3.4 3.4 0 0 0 0-6.8zM5.4 9.4l1.2 1.2-4 4-1.2-1.2z"/></svg>
        <span>www.<span class="web-accent">tarvellhomes</span>.example</span>
      </li>
    </ul>
    <p class="address">
      <svg viewBox="0 0 20 20" aria-hidden="true"><path d="M18 2L2 9l7 2 2 7z"/></svg>
      <span>2871 162nd Street Frank, Alberta</span>
    </p>
  </section>
</main>
</body>
</html>
```